Web Site

Target Market(s)

CEOs and International Sales & Marketing Directors of International Companies who wish to expand their business reach to Dubai and the Middle East and are looking for a local professional partner to work with.

Requirements
Must have
• Creativity is key. We don't want the normal standard boxes of text and boxes of pics. Be as creative as you like.
Nice to have
• (This is only a suggestion, we welcome your creativity)
- The center of all pages could be large rotating pictures which display professional corporate men/women working in an office, images of Dubai, the UAE, skyscrapers of business towers in Dubai, ..etc.
- Images should reflect Dubai and the Arab World as a modern, fast-paced, growing modern market - Not Traditional)
Should not have
• Not so colorful, the fewer colors you use, the better.
Not Crammed or Busy
Not Traditional but modern

```html
<!DOCTYPE html>
<html lang="en">
<head>
<meta charset="utf-8">
<title>Crest Group</title>
<link rel="stylesheet" href="https://fonts.googleapis.com/css2?family=Arimo:wght@400;700&family=Noto+Sans:wght@400;500&display=swap">
<style>
  :root {
    --brand-red: #7d2119;
    --brand-red-dark: #6a1a13;
    --page-bg: #f1f1f1;
    --panel-bg: #efefef;
    --tab-bg: #e2e2e2;
    --frame: #a9a9a9;
    --ink: #1e1e1e;
    --ink-soft: #333333;
    --rule: #1c1c1c;
    --white: #ffffff;
  }
  * { margin: 0; padding: 0; box-sizing: border-box; }
  html, body { width: 1200px; height: 1195px; overflow: hidden; }
  body {
    position: relative;
    background: var(--page-bg);
    font-family: "Arimo", Arial, sans-serif;
    color: var(--ink);
  }

  /* Header */
  .brand {
    position: absolute; left: 96px; top: 40px;
    display: flex; align-items: center; gap: 12px;
    font-family: "Arimo", Arial, sans-serif;
    font-weight: 400; font-size: 44px; letter-spacing: 1px;
    color: var(--ink);
  }
  .brand-mark { width: 16px; height: 16px; background: var(--brand-red); }
  .brand-name { line-height: 1; }

  .contact {
    position: absolute; left: 884px; top: 24px;
    display: grid; grid-template-columns: 63px auto; row-gap: 5px;
    font-size: 17px; line-height: 22px;
  }
  .contact dt { color: var(--brand-red); font-size: 19px; }
  .contact dd { color: var(--ink); font-size: 15.5px; padding-top: 1px; }

  /* Navigation */
  .site-rule { position: absolute; left: 0; width: 1200px; height: 2px; background: var(--rule); }
  .site-rule.top { top: 180px; }
  .main-nav {
    position: absolute; left: 76px; top: 135px; width: 1048px; height: 46px;
    background: var(--brand-red);
    border-radius: 3px 3px 0 0;
    display: flex; align-items: center; justify-content: space-between;
    padding: 0 7px 0 10px;
  }
  .main-nav a {
    color: var(--white); text-decoration: none;
    font-size: 14.5px; letter-spacing: 0;
    position: relative; white-space: nowrap;
  }
  .main-nav a.is-current::after {
    content: ""; position: absolute; left: 50%; top: 23px; margin-left: -7px;
    border-left: 7px solid transparent; border-right: 7px solid transparent;
    border-bottom: 7px solid var(--rule);
  }

  /* Hero */
  .hero {
    position: absolute; left: 76px; top: 192px; width: 1048px; height: 564px;
    border: 2px solid var(--frame); background: var(--panel-bg);
  }
  .hero-visual {
    position: absolute; left: 0; top: 0; width: 1044px; height: 449px;
    background: linear-gradient(180deg, #9fb1cd 0%, #8fa2bb 28%, #7d8a99 55%, #6f7b86 80%, #8a8f94 100%);
  }
  .slider-dots { position: absolute; right: 34px; top: 14px; display: flex; gap: 7px; }
  .slider-dots span { width: 12px; height: 12px; border-radius: 50%; background: #1c1c1c; }
  .slider-dots span:first-child { background: #4a4a4a; }
  .section-tab {
    position: absolute; background: var(--brand-red); color: var(--white);
    font-size: 20px; font-weight: 400; padding-left: 11px; border-radius: 4px 4px 0 0;
    display: flex; align-items: center;
  }
  .hero .section-tab { left: 18px; top: 408px; width: 133px; height: 41px; }
  .hero-copy {
    position: absolute; left: 21px; top: 464px; width: 900px;
    font-size: 16.3px; line-height: 21.8px; text-align: justify; color: var(--ink-soft);
    letter-spacing: 0.15px;
  }
  .hero-copy strong { font-weight: 400; color: #000; -webkit-text-stroke: 0.35px #000; }
  .btn-more {
    position: absolute; left: 949px; top: 478px; width: 66px; height: 35px;
    background: var(--brand-red); color: var(--white); border-radius: 3px;
    font-size: 16px; display: flex; align-items: center; justify-content: center;
  }

  /* What we do */
  .services-tab { left: 96px; top: 778px; width: 133px; height: 40px; }
  .services {
    position: absolute; left: 76px; top: 816px; width: 1048px; height: 266px;
    border: 2px solid var(--frame); background: var(--panel-bg);
  }
  .service-tabs {
    display: flex; height: 51px; background: var(--tab-bg);
    border-bottom: 1px solid #cfcfcf;
    font-family: "Noto Sans", Arial, sans-serif; font-size: 16px;
  }
  .service-tabs li {
    list-style: none; display: flex; align-items: center; justify-content: center;
    color: var(--brand-red); border-right: 1px solid #c8c8c8; white-space: nowrap;
  }
  .service-tabs li:last-child { border-right: none; }
  .service-tabs li.is-active { color: var(--ink); background: var(--tab-bg); position: relative; }
  .service-tabs li.is-active::after {
    content: ""; position: absolute; left: 15px; right: 11px; bottom: 7px; height: 2px; background: var(--ink);
  }
  .service-visual {
    position: absolute; left: 26px; top: 75px; width: 263px; height: 124px;
    border: 1px solid #bdbdbd;
    background: linear-gradient(120deg, #f4f4f4 0%, #cfcfcf 35%, #5a2a1e 60%, #2b1510 80%, #d9d9d9 100%);
    box-shadow: 0 6px 8px -4px rgba(0,0,0,0.25);
  }
  .service-title {
    position: absolute; left: 298px; top: 80px;
    font-family: "Noto Sans", Arial, sans-serif; font-size: 20px; font-weight: 400; color: var(--ink);
  }
  .service-copy {
    position: absolute; left: 300px; top: 109px; width: 722px;
    font-size: 16px; line-height: 21.8px; text-align: justify; color: var(--ink-soft); letter-spacing: 0.1px;
  }
  .btn-read {
    position: absolute; left: 911px; top: 202px; width: 103px; height: 32px;
    background: #222222; color: var(--white); border-radius: 16px;
    font-size: 16px; display: flex; align-items: center; justify-content: center;
  }

  /* Footer */
  .site-rule.bottom { top: 1108px; }
  .footer-links {
    position: absolute; left: 84px; top: 1124px;
    font-size: 13.5px; color: var(--ink); display: flex; gap: 0;
  }
  .footer-links a { color: var(--ink); text-decoration: none; }
  .footer-links .sep { margin: 0 7px; }
  .copyright { position: absolute; left: 862px; top: 1171px; font-size: 11.5px; color: var(--ink); }
</style>
</head>
<body>

<header class="site-header">
  <div class="brand"><span class="brand-mark"></span><span class="brand-name">CREST GROUP</span></div>
  <dl class="contact">
    <dt>Call</dt><dd>+9714 555 0142</dd>
    <dt>Email</dt><dd>info@crestgroup.example</dd>
  </dl>
  <nav class="main-nav">
    <a class="is-current" href="#">HOME</a>
    <a href="#">ABOUT THE GROUP</a>
    <a href="#">CHAIRMAN'S MESSAGE</a>
    <a href="#">DIVISIONS</a>
    <a href="#">GROUP COMPANIES</a>
    <a href="#">EMPLOYMENT &amp; ASSOCIATION</a>
    <a href="#">CONTACT US</a>
  </nav>
  <div class="site-rule top"></div>
</header>

<main>
  <section class="hero">
    <div class="hero-visual" role="img" aria-label="Aerial view of Dubai business towers and city skyline">
      <div class="slider-dots"><span></span><span></span><span></span></div>
    </div>
    <h2 class="section-tab">Welcome</h2>
    <p class="hero-copy"><strong>CREST group</strong> is a <strong>Dubai-based</strong> diversified groups of companies led by its chairman <strong>Sheikh Rashid bin Hamad Al Noori</strong>, a member of the <strong>Royal family of Dubai</strong>.The Group has grown with Dubai, and while best known for Real Estate Investment, it is globally recognized through its involvement in the Legal Consultations, Media Production, General Trading, and Telecommunication Services sectors.</p>
    <a class="btn-more">MORE</a>
  </section>

  <h2 class="section-tab services-tab">What we do</h2>
  <section class="services">
    <ul class="service-tabs">
      <li class="is-active" style="width:159px">Legal Consultation</li>
      <li style="width:154px">Marlo's Studios</li>
      <li style="width:228px">Crest Real Estate Investment</li>
      <li style="width:180px">Crest General Trading</li>
      <li style="width:191px">Crest Business Services</li>
      <li style="width:132px">Crest Telecom</li>
    </ul>
    <div class="service-visual" role="img" aria-label="Judge's gavel resting on a desk"></div>
    <h3 class="service-title">Legal Consultation</h3>
    <p class="service-copy">Lorem ipsum dolor sit amet, cu iracundia pertinacia pri. Cu sea causae utamur sensibus, id sint iusto regione cum. His ei epicuri noluisse appellantur, nec eruditi petentium expetenda ex. Ea graeci deleniti concludaturque nam. Sed veniam doctus suscipit te. Et nihil appareat recteque mei, meis option id pri. Pri in sumo enim invenire.</p>
    <a class="btn-read">Read more</a>
  </section>
</main>

<footer class="site-footer">
  <div class="site-rule bottom"></div>
  <nav class="footer-links">
    <a href="#">Home</a><span class="sep">|</span>
    <a href="#">About the Group</a><span class="sep">|</span>
    <a href="#">Privacy Policy</a><span class="sep">|</span>
    <a href="#">Sitemap</a><span class="sep">|</span>
    <a href="#">Terms of use</a><span class="sep">|</span>
    <a href="#">Contact us</a>
  </nav>
  <p class="copyright">Copyright 2012 Crest Group. All rights reserved.</p>
</footer>

</body>
</html>
```